Tallowbrook Paws Postboardly Ad

Need to incorporate the logo
Special postboardly discount - get $50 off any package (the main focus of the ad)
First walk free
link to website: www.tallowbrookpaws.com
tag: "is your dog a tallowbrookpaws?
Target Market(s)
The target audience is dog owners in Burnaby with a household income of 100,000 plus. People that can afford dogs but because they are working full-time or long hours are not able to.
Font styles to use
Sans Serif
Colors
acd036
Requirements
Must have
- Focus on the $50 off any package

```html
<!DOCTYPE html>
<html lang="en">
<head>
<meta charset="utf-8">
<title>Tallowbrook Paws – Postboardly Ad</title>
<link rel="stylesheet" href="https://fonts.googleapis.com/css2?family=Jost:wght@400;600&family=Open+Sans:wdth,wght@75,700;75,800;100,400&display=swap">
<style>
  :root {
    --page-bg: #8a8a8a;
    --sage: #cdd89c;
    --slate: #4a4a52;
    --olive: #8ea226;
    --white: #ffffff;
    --ink: #46464e;
    --ink-soft: #4f4f57;
  }
  * { box-sizing: border-box; margin: 0; padding: 0; }
  html, body {
    width: 1200px; height: 985px; overflow: hidden;
    background: var(--page-bg);
  }
  .ad {
    position: absolute; left: 56px; top: 119px;
    width: 1088px; height: 747px;
    display: flex; flex-direction: column;
    box-shadow: 0 6px 18px rgba(0,0,0,.35);
  }
  .band { display: flex; flex-direction: column; align-items: center; justify-content: center; text-align: center; }

  .tagline {
    height: 256px; background: radial-gradient(ellipse at 50% 40%, #d6e0a8 0%, var(--sage) 70%);
    font-family: "Jost", sans-serif; color: var(--ink); text-transform: uppercase; line-height: 1.08;
  }
  .tagline__lead { font-size: 70px; font-weight: 400; }
  .tagline__brand { font-size: 66px; font-weight: 400; }
  .tagline__brand strong { font-weight: 600; }

  .offer {
    height: 267px; background: var(--slate); color: var(--white);
    font-family: "Open Sans", sans-serif; font-stretch: 75%; font-weight: 700; text-transform: uppercase;
    text-shadow: 3px 4px 6px rgba(0,0,0,.7);
  }
  .offer__label { font-size: 46px; line-height: 1; margin-bottom: 6px; }
  .offer__headline { display: flex; align-items: baseline; gap: 22px; line-height: 1; }
  .offer__minor { font-size: 78px; }
  .offer__major { font-size: 114px; font-weight: 800; }

  .website {
    height: 133px; background: radial-gradient(ellipse at 50% 50%, #98ad2e 0%, var(--olive) 70%);
    color: var(--white); font-family: "Open Sans", sans-serif; font-stretch: 100%; font-weight: 400; text-transform: uppercase;
  }
  .website__note { font-size: 22px; line-height: 1.2; }
  .website__url { font-size: 39px; line-height: 1.2; letter-spacing: .5px; }

  .brand {
    height: 91px; background: var(--white);
    flex-direction: row; gap: 18px;
  }
  .brand__mark { width: 40px; height: 40px; border-radius: 50%; background: var(--olive); }
  .brand__name { font-family: "Jost", sans-serif; font-weight: 400; font-size: 40px; color: var(--ink-soft); text-transform: uppercase; letter-spacing: 1px; }
</style>
</head>
<body>
  <main class="ad">
    <section class="band tagline">
      <p class="tagline__lead">Is your dog a</p>
      <p class="tagline__brand"><strong>Tallowbrookpaws</strong> dog?</p>
    </section>

    <section class="band offer">
      <p class="offer__label">Special Postboardly Discount</p>
      <p class="offer__headline">
        <span class="offer__minor">Get</span>
        <span class="offer__major">$50 Off</span>
        <span class="offer__minor">Any Package</span>
      </p>
    </section>

    <section class="band website">
      <p class="website__note">First walk free to our website</p>
      <p class="website__url">www.tallowbrookpaws.com</p>
    </section>

    <footer class="band brand">
      <span class="brand__mark" aria-hidden="true"></span>
      <span class="brand__name">Tallowbrook Paws</span>
    </footer>
  </main>
</body>
</html>
```